Web design for a relaunch of a technology and knowledge transfer company

Design for the relaunch of an existing website The company specializes in technology and knowledge transfer between companies (and universities). The innovation company (company name) combines many years of experience in technology transfer, innovation management, project management and grant applications. Link: http://www.vorlaufwerkstatt.example The colors of the logo are not very advantageous and can be adjusted a bit. There are currently no picture worlds, these are to be selected by the designer. Abstract motifs are certainly an advantage here (10 motifs). Animated programming could be done (network etc. http://pelvart.qmstudio.example/). In this case a suggestion is made, which we convert programming technically. The structure and contents of the existing pages will be adopted and supplemented. The programming will be done with TYPO3 in responsive form (bootstrap). Required are start page, content page and contact page. -------------------------------------------------- ------------------------------ Web design for a relaunch of a company in technology and knowledge transfer Design for the relaunch of an existing website. The company specializes in technology and knowledge transfer between companies (and universities). The innovation company combines many years of experience in the fields of technology transfer, innovation management, project management and grant application. Link: http://www.vorlaufwerkstatt.example The color of the logo is not exactly advantageous and can be adjusted. There are currently no image worlds, these are to be selected by the designer. Abstract motifs are certainly an advantage here (10 motifs). It could also be made animated programming (network, etc. http://pelvart.qmstudio.example/). In this case, a proposal has to be made, which we implement in terms of programming technology. The structure and contents of the existing pages are taken over and supplemented. Programming is done with TYPO3 in responsive form (bootstrap). Required are homepage, content page and contact page.

```html
<!DOCTYPE html>
<html lang="en">
<head>
<meta charset="utf-8">
<title>Vorlaufwerkstatt – Technology and Knowledge Transfer</title>
<link rel="stylesheet" href="https://fonts.googleapis.com/css2?family=Roboto:wght@300;400;500;700&display=swap">
<style>
:root{
  --blue:#1f1f9c;
  --blue-deep:#12127a;
  --navy:#0b0f3d;
  --red:#e3122b;
  --ink:#1b1b1b;
  --grey:#6f6f6f;
  --light:#f1f1f1;
  --faint:#e4e4e4;
  --white:#ffffff;
}
*{margin:0;padding:0;box-sizing:border-box}
html,body{width:1200px;height:3309px;overflow:hidden;background:var(--white)}
body{font-family:'Roboto',Arial,sans-serif;color:var(--ink);position:relative}
.abs{position:absolute}
a{color:inherit;text-decoration:none}

/* header */
.topline{left:0;top:0;width:1200px;height:4px;background:var(--red)}
.brand{display:flex;align-items:center;gap:12px;font-size:17px;font-weight:500;letter-spacing:.5px}
.brand .mark{width:22px;height:22px;background:var(--red)}
.header-brand{left:145px;top:60px;color:var(--blue)}
.contact-bar{top:20px;left:598px;display:flex;gap:30px;font-size:15px;color:var(--red);align-items:center}
.contact-bar span{display:flex;align-items:center;gap:12px}
.ico-box{width:30px;height:30px;border:2px solid var(--red);border-radius:4px;display:flex;align-items:center;justify-content:center}
.ico-box.fill{background:var(--blue-deep);border-color:var(--blue-deep)}
.main-nav{top:70px;left:485px;display:flex;gap:34px;font-size:14.5px;font-weight:500;text-transform:uppercase}

/* hero */
.hero{left:0;top:105px;width:1200px;height:680px;background:linear-gradient(100deg,#0a1a2e 0%,#0f3247 35%,#0a1f30 60%,#05101c 100%)}
.hero-visual{left:0;top:105px;width:720px;height:680px;background:radial-gradient(circle at 330px 340px,#5da9c4 0%,#2a6f8c 28%,#12384f 55%,rgba(10,26,46,0) 75%)}
.hero-title{left:545px;top:308px;width:510px;height:60px;background:var(--blue);color:var(--white);font-size:38px;font-weight:500;display:flex;align-items:center;justify-content:center}
.hero-text{left:520px;top:388px;width:535px;text-align:right;color:var(--white);font-size:19.5px;font-weight:500;line-height:31px}
.btn{background:var(--red);color:var(--white);font-weight:500;text-transform:uppercase;border-radius:30px;display:flex;align-items:center;justify-content:center;gap:10px}
.hero-btn{left:895px;top:505px;width:160px;height:48px;font-size:18px}
.hero-curve{left:0;top:600px}
.mouse{left:575px;top:660px;width:50px;height:66px}

/* services */
.section-title{font-size:44px;font-weight:500;text-align:center;width:1200px;left:0;color:var(--ink)}
.services-title{top:782px}
.services-intro{left:280px;top:862px;width:640px;text-align:center;font-size:14.5px;line-height:30px;color:var(--grey)}
.ghost-vertical{left:1083px;top:1265px;transform:rotate(-90deg);transform-origin:left top;font-size:88px;font-weight:700;color:var(--faint);letter-spacing:2px}
.card{width:415px;height:162px;padding:20px 0 0 22px;display:flex;gap:26px}
.card.active{background:var(--white);box-shadow:0 0 14px rgba(0,0,0,.25)}
.card .icon{width:100px;height:100px;flex:none}
.card h3{font-size:17px;font-weight:500;line-height:24px;margin-top:8px}
.card p{font-size:12.5px;color:var(--grey);line-height:24px;margin-top:6px;width:245px}
.card .more{font-size:12.5px;font-weight:500;color:var(--red);margin-top:4px;display:block}
.card-1{left:175px;top:978px}
.card-2{left:635px;top:978px}
.card-3{left:175px;top:1160px}
.card-4{left:635px;top:1160px}
.view-btn{left:505px;top:1358px;width:190px;height:48px;font-size:19px}

/* moments */
.moments{left:0;top:1495px;width:1200px;height:530px;background:linear-gradient(135deg,#ededed,#f7f7f7 45%,#eaeaea)}
.moments-ghost{left:636px;top:1582px;font-size:80px;font-weight:700;color:#dcdcdc}
.moments-title{left:143px;top:1588px;font-size:31px;font-weight:500;line-height:40px}
.rule{left:143px;top:1680px;width:36px;height:4px;background:var(--blue)}
.q-list{list-style:none;font-size:13.5px;color:#333;line-height:33px}
.q-list li{position:relative;padding-left:16px}
.q-list li::before{content:"";position:absolute;left:0;top:12px;width:10px;height:10px;border-radius:50%;background:var(--red)}
.q-left{left:143px;top:1720px;width:420px}
.q-right{left:603px;top:1720px;width:445px}

/* reports */
.events-ghost{left:-10px;top:2090px;font-size:88px;font-weight:700;color:#ececec}
.reports-title{top:2088px;font-size:44px;line-height:57px}
.photo{background:linear-gradient(160deg,#c9c4bd,#8a8580 55%,#4d4a48)}
.lead-photo{left:155px;top:2258px;width:457px;height:279px;border-radius:3px}
.lead-title{left:155px;top:2560px;font-size:22px;font-weight:500}
.date{display:flex;align-items:center;gap:8px;font-size:13px;color:#333}
.lead-date{left:155px;top:2600px}
.lead-text{left:155px;top:2634px;width:420px;font-size:13px;line-height:25px;color:#555}
.lead-btn{left:155px;top:2728px;width:130px;height:40px;font-size:13px}
.item-photo{left:648px;width:170px;height:150px;border-radius:3px}
.item-title{left:840px;width:215px;font-size:15px;font-weight:500;line-height:24px;text-transform:uppercase}
.arrows{left:1020px;top:2748px;display:flex;gap:12px}

/* footer */
.footer-bg{left:0;top:2790px;width:1200px;height:519px}
.footer-badge{left:568px;top:2860px;width:64px;height:64px;border-radius:50%;background:var(--white)}
.footer-brand{left:145px;top:3050px;color:var(--white)}
.footer-brand .mark{background:var(--white)}
.f-head{font-size:17px;font-weight:500;color:var(--white);text-transform:uppercase}
.f-list{list-style:none;color:var(--white);font-size:13px;line-height:28.5px}
.f-contact li{display:flex;gap:18px;line-height:22px;margin-bottom:12px}
.f-links li::before{content:"»";margin-right:14px}
.social li{display:flex;align-items:center;gap:12px;margin-bottom:12px}
.social .circle{width:42px;height:42px;border-radius:50%;border:2px solid var(--white)}
.f-line{left:145px;top:3218px;width:910px;height:1px;background:rgba(255,255,255,.35)}
.copyright{left:0;top:3253px;width:1200px;text-align:center;color:var(--white);font-size:12px}
</style>
</head>
<body>

<div class="abs topline"></div>
<header>
  <div class="abs brand header-brand"><span class="mark"></span>VORLAUFWERKSTATT</div>
  <div class="abs contact-bar">
    <span><span class="ico-box"><svg width="16" height="16" viewBox="0 0 24 24"><path d="M6.6 10.8a15 15 0 006.6 6.6l2.2-2.2a1 1 0 011-.3 11.4 11.4 0 003.6.6 1 1 0 011 1V20a1 1 0 01-1 1A17 17 0 013 4a1 1 0 011-1h3.5a1 1 0 011 1 11.4 11.4 0 00.6 3.6 1 1 0 01-.3 1z" fill="#e3122b"/></svg></span><span style="color:var(--blue-deep)">+49 5550 10 20 300</span></span>
    <span><span class="ico-box fill"><svg width="16" height="12" viewBox="0 0 16 12"><rect x="0" y="0" width="16" height="12" fill="#fff"/><path d="M0 0l8 6 8-6" fill="none" stroke="#12127a" stroke-width="1.5"/></svg></span>info@vorlaufwerkstatt.example</span>
  </div>
  <nav class="abs main-nav"><a>Services</a><a>References</a><a>Events &amp; Workshops</a><a>Reports</a><a>Contact</a></nav>
</header>

<section>
  <div class="abs hero"></div>
  <div class="abs hero-visual" role="img" aria-label="Hands holding a glowing network globe with two light bulbs, abstract technology motif"></div>
  <div class="abs hero-title">THE VORLAUF WORKSHOP</div>
  <p class="abs hero-text">Is a technology and knowledge transfer company that supports companies in implementing their innovative ideas. We use our large network of scientific institutions.</p>
  <a class="abs btn hero-btn">Read more</a>
  <svg class="abs hero-curve" width="1200" height="190" viewBox="0 0 1200 190"><path d="M0 190V170Q600 -30 1200 170V190Z" fill="#fff"/></svg>
  <svg class="abs mouse" viewBox="0 0 50 66"><circle cx="25" cy="30" r="25" fill="#fff"/><rect x="18" y="12" width="14" height="22" rx="7" fill="none" stroke="#222" stroke-width="1.6"/><line x1="25" y1="16" x2="25" y2="21" stroke="#222" stroke-width="1.6"/><path d="M20 40l5 4 5-4M20 45l5 4 5-4" fill="none" stroke="#222" stroke-width="1.4"/></svg>
</section>

<section>
  <h2 class="abs section-title services-title">SERVICES</h2>
  <p class="abs services-intro">The innovation company brings together over 15 years of experience in the areas of technology transfer, innovation management, project management and grant application</p>
  <div class="abs ghost-vertical">SERVICES</div>

  <article class="abs card card-1 active">
    <svg class="icon" viewBox="0 0 78 80"><rect x="18" y="20" width="56" height="56" rx="4" fill="none" stroke="#1f1f9c" stroke-width="2.5"/><circle cx="46" cy="48" r="13" fill="none" stroke="#e3122b" stroke-width="2"/><path d="M33 48h26M46 35c-6 8-6 18 0 26M46 35c6 8 6 18 0 26" fill="none" stroke="#e3122b" stroke-width="1.6"/></svg>
    <div><h3>Technology and<br>knowledge transfer</h3><p>We support companies in implementing their innovative projects.Since innovations,</p><a class="more">READ MORE</a></div>
  </article>
  <article class="abs card card-2">
    <svg class="icon" viewBox="0 0 78 80"><rect x="18" y="20" width="56" height="56" rx="4" fill="none" stroke="#1f1f9c" stroke-width="2.5"/><rect x="32" y="36" width="28" height="20" fill="none" stroke="#e3122b" stroke-width="2"/><path d="M36 52l7-7 5 4 8-8M46 56v8M40 64h12" fill="none" stroke="#e3122b" stroke-width="1.6"/></svg>
    <div><h3>Innovation and project<br>management</h3><p>The management of innovation processes in the sense of a systematic planning,</p><a class="more">READ MORE</a></div>
  </article>
  <article class="abs card card-3">
    <svg class="icon" viewBox="0 0 78 80"><rect x="18" y="20" width="56" height="56" rx="4" fill="none" stroke="#1f1f9c" stroke-width="2.5"/><circle cx="46" cy="48" r="6" fill="none" stroke="#e3122b" stroke-width="2"/><g fill="none" stroke="#e3122b" stroke-width="1.6"><circle cx="34" cy="36" r="3"/><circle cx="58" cy="36" r="3"/><circle cx="34" cy="60" r="3"/><circle cx="58" cy="60" r="3"/><path d="M36 38l6 6M56 38l-6 6M36 58l6-6M56 58l-6-6"/></g></svg>
    <div><h3>Cooperation and network<br>management</h3><p>We support companies in implementing their innovative projects.Since innovations,</p><a class="more">READ MORE</a></div>
  </article>
  <article class="abs card card-4">
    <svg class="icon" viewBox="0 0 78 80"><rect x="18" y="20" width="56" height="56" rx="4" fill="none" stroke="#1f1f9c" stroke-width="2.5"/><path d="M46 32a12 12 0 00-7 22v6h14v-6a12 12 0 00-7-22z" fill="none" stroke="#e3122b" stroke-width="2"/><path d="M50 42a5 5 0 100 6" fill="none" stroke="#e3122b" stroke-width="1.6"/><path d="M41 64h10" stroke="#e3122b" stroke-width="1.6"/></svg>
    <div><h3>Property Rights and Co.</h3><p>As soon as an idea is transformed into a product or process innovation, protection rights are often affected.</p><a class="more">READ MORE</a></div>
  </article>

  <a class="abs btn view-btn">View more <svg width="18" height="18" viewBox="0 0 18 18"><circle cx="9" cy="9" r="9" fill="#fff"/><path d="M5 9h7M9 5.5L12.5 9 9 12.5" fill="none" stroke="#e3122b" stroke-width="2"/></svg></a>
</section>

<section>
  <div class="abs moments"></div>
  <svg class="abs" style="left:0;top:1930px" width="1200" height="100" viewBox="0 0 1200 100"><path d="M0 100V20Q600 130 1200 20V100Z" fill="#fff"/></svg>
  <div class="abs moments-ghost">MOMENTS</div>
  <h2 class="abs moments-title">MAYBE YOU'VE ALREADY<br>WONDERED IN SOME MOMENTS</h2>
  <div class="abs rule"></div>
  <ul class="abs q-list q-left">
    <li>With whom can I implement my innovative idea?</li>
    <li>Who helps me develop new products, services or business models based on my abilities?</li>
    <li>How do I become more independent of my existing customers with my own products?</li>
    <li>Who protects my ideas?</li>
  </ul>
  <ul class="abs q-list q-right">
    <li>Who opens the doors to science for me if I do not know who the right people are?</li>
    <li>How can I get the latest insights for improving my business processes and who can help me with the implementation in my own company?</li>
    <li>Who relieves me in carrying out cooperation projects with science?</li>
    <li>Where and how do I get impulses for new things?</li>
  </ul>
</section>

<section>
  <div class="abs events-ghost">EVENTS</div>
  <h2 class="abs section-title reports-title">REPORTS ON CURRENT<br>TOPICS &amp; EVENTS</h2>

  <div class="abs photo lead-photo" role="img" aria-label="Speaker presenting in a lecture hall in front of a projection screen"></div>
  <h3 class="abs lead-title">IOT - WHAT COMPANIES WANT</h3>
  <div class="abs date lead-date"><svg width="12" height="12" viewBox="0 0 12 12"><rect x="1" y="2" width="10" height="9" fill="none" stroke="#e3122b" stroke-width="1.5"/><path d="M1 5h10M4 0v3M8 0v3" stroke="#e3122b" stroke-width="1.5"/></svg>09/10/2018</div>
  <p class="abs lead-text">Lorem Ipsum is simply dummy text of the printing and typesetting industry. Lorem Ipsum has been the industry's standard dummy text ever since the 1500s, when an unknown printer</p>
  <a class="abs btn lead-btn">Read more</a>

  <div class="abs photo item-photo" style="top:2260px" role="img" aria-label="Conference participants talking at a founders meetup"></div>
  <h3 class="abs item-title" style="top:2280px">Ideaforge meetup on the 5th and 6th of September in Brenstadt</h3>
  <div class="abs date" style="left:840px;top:2368px"><svg width="12" height="12" viewBox="0 0 12 12"><rect x="1" y="2" width="10" height="9" fill="none" stroke="#e3122b" stroke-width="1.5"/><path d="M1 5h10M4 0v3M8 0v3" stroke="#e3122b" stroke-width="1.5"/></svg>09/10/2018</div>

  <div class="abs photo item-photo" style="top:2428px" role="img" aria-label="Visitors in a research laboratory"></div>
  <h3 class="abs item-title" style="top:2448px">In conversation with the Nordtal Research Institute</h3>
  <div class="abs date" style="left:840px;top:2536px"><svg width="12" height="12" viewBox="0 0 12 12"><rect x="1" y="2" width="10" height="9" fill="none" stroke="#e3122b" stroke-width="1.5"/><path d="M1 5h10M4 0v3M8 0v3" stroke="#e3122b" stroke-width="1.5"/></svg>09/10/2018</div>

  <div class="abs photo item-photo" style="top:2595px" role="img" aria-label="Workshop participants seated around a table"></div>
  <h3 class="abs item-title" style="top:2626px">Embedded engineering discussions IV</h3>
  <div class="abs date" style="left:840px;top:2690px"><svg width="12" height="12" viewBox="0 0 12 12"><rect x="1" y="2" width="10" height="9" fill="none" stroke="#e3122b" stroke-width="1.5"/><path d="M1 5h10M4 0v3M8 0v3" stroke="#e3122b" stroke-width="1.5"/></svg>09/10/2018</div>

  <div class="abs arrows"><svg width="12" height="18" viewBox="0 0 12 18"><path d="M10 2L3 9l7 7" fill="none" stroke="#1f1f9c" stroke-width="2.5"/></svg><svg width="12" height="18" viewBox="0 0 12 18"><path d="M2 2l7 7-7 7" fill="none" stroke="#e3122b" stroke-width="2.5"/></svg></div>
</section>

<footer>
  <svg class="abs footer-bg" width="1200" height="519" viewBox="0 0 1200 519"><defs><radialGradient id="fg" cx="0.3" cy="0.8" r="0.9"><stop offset="0" stop-color="#2f2fc2"/><stop offset="0.6" stop-color="#1a1a9a"/><stop offset="1" stop-color="#10107a"/></radialGradient></defs><path d="M0 0Q600 190 1200 0V519H0Z" fill="url(#fg)"/></svg>
  <div class="abs footer-badge"></div>
  <div class="abs brand footer-brand"><span class="mark"></span>VORLAUFWERKSTATT</div>

  <div class="abs f-head" style="left:450px;top:2985px">Contact us</div>
  <ul class="abs f-list f-contact" style="left:450px;top:3028px;width:260px">
    <li><svg width="14" height="14" viewBox="0 0 14 14"><path d="M7 1L0 7h2v6h4V9h2v4h4V7h2z" fill="#fff"/></svg><span>Vorlauf Workshop for<br>University and Business Management<br>Lindenweg 8, 31000 Musterdorf</span></li>
    <li><svg width="14" height="14" viewBox="0 0 14 14"><rect x="3" y="0" width="8" height="14" rx="1.5" fill="#fff"/></svg><span>Tel. +49 5550 10 20 300</span></li>
    <li><svg width="14" height="14" viewBox="0 0 14 14"><rect x="0.5" y="2.5" width="13" height="9" fill="none" stroke="#fff"/><path d="M0.5 2.5l6.5 5 6.5-5" fill="none" stroke="#fff"/></svg><span>info@vorlaufwerkstatt.example</span></li>
  </ul>

  <div class="abs f-head" style="left:760px;top:2985px">Quick links</div>
  <ul class="abs f-list f-links" style="left:760px;top:3024px">
    <li>Services</li><li>References</li><li>Events &amp; Workshops</li><li>Reports</li><li>Contact</li>
  </ul>

  <div class="abs f-head" style="left:955px;top:2985px">Follow us</div>
  <ul class="abs f-list social" style="left:955px;top:3036px">
    <li><span class="circle"></span>Facepage</li>
    <li><span class="circle"></span>Linkfolio</li>
  </ul>

  <div class="abs f-line"></div>
  <p class="abs copyright">© copyright 2019 Companyname . All rights reserved &nbsp;|&nbsp; Privacy ploicy</p>
</footer>

</body>
</html>
```